Harwick Oates - Facebook Cover Photo & Photo Icon Design

We’re looking for a Facebook Cover Photo and Profile Icon design for Harwick Oates, a leading Residential Real Estate brand under Harwick Property Agents, based in Capalaba and Alexandra Hills, Queensland, Australia.

This design will represent my professional real estate profile and needs to be bold, clean, and on-brand.

Deliverables:

Facebook Cover Photo (820 x 312 px, optimized for mobile + desktop)

Facebook Profile Icon (1:1 ratio, minimum 320 x 320 px)

Design Guidelines:

1. Must Include:

The Harwick Oates logo (provided after project start)

Use of the Harwick Property Agents brand colour palette (will be supplied)

Clear connection to residential real estate

2. Optional but Preferred:

A local photo or skyline of Capalaba or Alexandra Hills in QLD (bonus points for this)

Space for a short tagline like:
“Selling Faster. Selling Smarter. Selling Harwick.”
(Optional tagline – open to variations if it improves layout/design)

3. Style & Feel:

Professional yet personable

Clean, modern aesthetic

Subtle touches of fun or personality are welcome

Layout must work well when overlaid by Facebook UI elements (like profile photo & call-to-action buttons)

Who I Am:
I'm a well-known residential real estate agent in the Redlands area, known for high-energy campaigns, premium video marketing, and a results-driven approach. My brand is fun, fresh, and high-performing — just like the real estate campaigns I run.

Files to be Provided (after selection):

Harwick Oates logo in high-res

Brand colour palette / style reference

Optional photo references if local imagery is not sourced by designer

Final Notes:

Make sure all text is legible on mobile and desktop

Original, layered design files must be delivered (PSD or AI preferred)

Bonus points if it feels uniquely “Bayside Queensland” while maintaining a national-level professional polish

Target Market(s)

Alexandra Hills, Capalaba & Sheldon

Industry/Entity Type

Real Estate

Colors
0054AA
0677BA
7BADD7
CADEEF
E8F1F8

Requirements
Must have
• Headshot, Mobile Number 0491 726 055, Suburbs - Alexandra Hills, Capalaba & Sheldon
Nice to have
• White, Crisp & Professional. Bottom Banner with Suburb List. Specialising in Alexandra Hills, Capalaba & Sheldon

```html
<!DOCTYPE html>
<html lang="en">
<head>
<meta charset="utf-8">
<title>Harwick Oates – Facebook Cover &amp; Profile Icon Set</title>
<link rel="stylesheet" href="https://fonts.googleapis.com/css2?family=Oswald:wght@400;500;600;700&family=Montserrat:wght@600;700&family=Arimo:wght@700&display=swap">
<style>
  :root {
    --royal: #2d2aa6;
    --royal-deep: #1f1c82;
    --navy: #1c1f6e;
    --gold: #ffc400;
    --tan: #b58d4e;
    --ink: #141414;
    --white: #ffffff;
    --lavender: #b9bde6;
    --suit-a: #44526f;
    --suit-b: #2a3550;
  }
  * { margin: 0; padding: 0; box-sizing: border-box; }
  html, body { width: 870px; height: 1200px; overflow: hidden; background: var(--white); }
  .sheet {
    position: relative; width: 1274px; height: 1756px;
    transform: scale(0.68289); transform-origin: 0 0;
    border: 2px solid var(--ink); background: var(--white);
    font-family: "Oswald", sans-serif;
  }
  .abs { position: absolute; }
  .size-label { position: absolute; font-family: "Arimo", sans-serif; font-weight: 700; font-size: 28px; color: var(--ink); white-space: nowrap; }

  .panel { position: absolute; overflow: hidden; background: linear-gradient(135deg, var(--royal) 0%, var(--royal-deep) 100%); }
  .panel > * { z-index: 2; }
  .panel > .white-wedge { z-index: 0; }
  .panel > .portrait { z-index: 1; }
  .white-wedge { position: absolute; inset: 0; }
  .portrait { position: absolute; border-radius: 45% 45% 0 0 / 30% 30% 0 0;
    background: linear-gradient(180deg, #7a6a62 0%, var(--suit-a) 35%, var(--suit-b) 100%); }

  .wordmark { position: absolute; background: var(--white); display: flex; align-items: center; justify-content: center;
    color: var(--navy); font-weight: 500; white-space: nowrap; }

  .headline { position: absolute; text-align: center; color: var(--white); font-weight: 700; line-height: 0.98;
    text-shadow: 2px 3px 0 rgba(0,0,0,0.55); transform: rotate(-4deg); text-transform: uppercase; white-space: nowrap; }
  .tag { position: absolute; background: var(--gold); color: var(--navy); font-weight: 500; display: flex; white-space: nowrap;
    align-items: center; justify-content: center; transform: rotate(-4deg); box-shadow: 2px 3px 0 rgba(0,0,0,0.35); }
  .accent-bar { position: absolute; background: var(--gold); transform: skewX(-20deg) rotate(-4deg); }
  .chevrons { position: absolute; color: var(--white); letter-spacing: -2px; }

  .follow { position: absolute; font-family: "Montserrat", sans-serif; font-weight: 700; color: var(--white); letter-spacing: 1px; white-space: nowrap; }
  .social-row { position: absolute; display: flex; }
  .social-dot { border-radius: 50%; background: var(--gold); }
  .rule-v { position: absolute; background: var(--tan); }
  .suburbs { position: absolute; color: var(--white); font-weight: 500; line-height: 1.2; text-shadow: 1px 2px 0 rgba(0,0,0,0.4); white-space: nowrap; }
  .underline { position: absolute; background: var(--gold); }

  .cta { position: absolute; display: flex; align-items: center; }
  .cta-icon { background: #3a1a0e; display: flex; align-items: center; justify-content: center; border-radius: 3px; }
  .cta-pill { background: var(--gold); color: var(--ink); font-weight: 500; display: flex; align-items: center; justify-content: center; border-radius: 0 4px 4px 0; white-space: nowrap; }
  .phone-line { position: absolute; color: var(--ink); font-weight: 600; letter-spacing: 1px; white-space: nowrap; }
  .web-line { position: absolute; color: var(--ink); font-weight: 600; white-space: nowrap; }

  .services-title { position: absolute; color: var(--white); font-weight: 500; font-size: 18px; white-space: nowrap; }
  .services-box { position: absolute; background: var(--gold); border-radius: 8px 14px 8px 8px; box-shadow: 3px 4px 0 rgba(0,0,0,0.4); }
  .services-box ol { list-style: none; padding: 10px 0 0 12px; }
  .services-box li { font-size: 10px; font-weight: 600; color: var(--navy); height: 22.4px; line-height: 22.4px; white-space: nowrap; }

  .card-name { position: absolute; color: var(--gold); font-weight: 600; font-size: 70px; line-height: 1; text-shadow: 2px 3px 0 rgba(0,0,0,0.4); white-space: nowrap; }
  .card-role { position: absolute; color: var(--white); font-weight: 500; font-size: 40px; line-height: 1; white-space: nowrap; }
  .contact-row { position: absolute; left: 158px; display: flex; align-items: center; }
  .contact-dot { width: 34px; height: 34px; border-radius: 50%; background: var(--gold); border: 2px solid var(--ink); display: flex; align-items: center; justify-content: center; }
  .contact-text { margin-left: 24px; color: var(--white); font-weight: 500; font-size: 27px; letter-spacing: 1.5px; white-space: nowrap; }
  .suburb-band { position: absolute; left: 0; right: 0; bottom: 0; height: 70px; background: var(--white); display: flex; align-items: center; padding-left: 36px; gap: 24px; color: var(--navy); font-weight: 600; font-size: 28px; white-space: nowrap; }

  .footer { position: absolute; left: 0; right: 0; top: 1663px; height: 91px; border-top: 3px solid var(--ink); display: flex; }
  .footer-left { width: 432px; background: var(--white); display: flex; align-items: center; justify-content: center; font-weight: 600; font-size: 38px; color: var(--ink); white-space: nowrap; }
  .footer-right { flex: 1; background: var(--ink); color: var(--white); display: flex; align-items: center; justify-content: center; font-weight: 500; font-size: 30px; white-space: nowrap; }
</style>
</head>
<body>
<div class="sheet">

  <!-- Desktop cover -->
  <div class="size-label" style="left:108px; top:63px;">Desktop: 820 x 312 px</div>
  <section class="panel desktop-cover" style="left:110px; top:115px; width:821px; height:312px;">
    <svg class="white-wedge" width="821" height="312"><polygon points="821,186 821,312 560,312" fill="#fff"/></svg>
    <div class="portrait" role="img" aria-label="Headshot of the agent in a navy blazer and white shirt" style="left:345px; top:28px; width:255px; height:284px;"></div>
    <div class="wordmark" style="left:0; top:16px; width:105px; height:46px; border-radius:0 10px 10px 0; font-size:14px;">HARWICK OATES</div>

    <div class="services-title" style="left:35px; top:127px;">OUR SERVICES :</div>
    <svg class="abs" style="left:20px; top:165px;" width="120" height="135"><path d="M6 2 V95 Q6 127 38 127 H108" fill="none" stroke="#fff" stroke-width="2"/></svg>
    <div class="services-box" style="left:47px; top:153px; width:118px; height:129px;">
      <ol><li>1. LOREM IPSUM DOREM</li><li>2. LOREM IPSUM DOREM</li><li>3. LOREM IPSUM DOREM</li><li>4. LOREM IPSUM DOREM</li><li>5. LOREM IPSUM DOREM</li></ol>
    </div>
    <div class="chevrons" style="left:140px; top:284px; font-size:11px;">◀◀◀</div>

    <div class="chevrons" style="left:247px; top:48px; font-size:15px;">▶▶▶</div>
    <div class="accent-bar" style="left:305px; top:52px; width:70px; height:6px;"></div>
    <div class="headline" style="left:200px; top:64px; width:220px; font-size:44px;">Harwick<br>Properties<br>Agency</div>
    <div class="tag" style="left:245px; top:205px; width:142px; height:36px; font-size:19px;">-HARWICK OATES</div>

    <div class="follow" style="left:686px; top:16px; font-size:10.5px;">FOLLOW US ON</div>
    <div class="social-row" style="left:691px; top:32px; gap:8px;">
      <span class="social-dot" style="width:16px;height:16px;"></span><span class="social-dot" style="width:16px;height:16px;"></span><span class="social-dot" style="width:16px;height:16px;"></span><span class="social-dot" style="width:16px;height:16px;"></span>
    </div>
    <div class="rule-v" style="left:795px; top:35px; width:3px; height:145px;"></div>
    <div class="suburbs" style="left:596px; top:82px; font-size:21px;">- ALEXANDRA HILLS<br>- CAPALABA<br>- SHELDON</div>
    <div class="underline" style="left:610px; top:166px; width:80px; height:4px;"></div>
    <svg class="abs" style="left:540px; top:105px;" width="80" height="140">
      <path d="M50 135 Q80 80 25 40 Q15 30 32 20" fill="none" stroke="#fff" stroke-width="1.6" stroke-dasharray="5 4"/>
      <polygon points="30,10 58,18 34,30" fill="#fff"/>
    </svg>
    <div class="cta" style="left:698px; top:238px; height:24px;">
      <div class="cta-icon" style="width:24px;height:24px;"><svg width="12" height="12"><path d="M1 6 H10 M6 2 L10 6 L6 10" stroke="#fff" stroke-width="2" fill="none"/></svg></div>
      <div class="cta-pill" style="width:75px;height:24px;font-size:11px;">CONTACT US</div>
    </div>
    <div class="phone-line" style="left:698px; top:264px; font-size:16px;">0491-726-055</div>
    <div class="web-line" style="left:678px; top:284px; font-size:11px;">WWW.YOURWEBSITE.COM</div>
  </section>

  <!-- Mobile cover -->
  <div class="size-label" style="left:108px; top:478px;">Mobile: 640 x 360 px</div>
  <section class="panel mobile-cover" style="left:110px; top:527px; width:642px; height:361px; border:1px solid var(--navy);">
    <svg class="white-wedge" width="642" height="361"><polygon points="642,220 642,361 455,361" fill="#fff"/></svg>
    <div class="portrait" role="img" aria-label="Headshot of the agent in a navy blazer and white shirt" style="left:205px; top:42px; width:265px; height:319px;"></div>
    <div class="wordmark" style="left:0; top:14px; width:95px; height:40px; border-radius:0 10px 10px 0; font-size:13px;">HARWICK OATES</div>

    <div class="chevrons" style="left:104px; top:70px; font-size:16px;">▶▶▶</div>
    <div class="accent-bar" style="left:156px; top:72px; width:76px; height:6px;"></div>
    <div class="headline" style="left:45px; top:82px; width:240px; font-size:48px;">Harwick<br>Properties<br>Agency</div>
    <div class="tag" style="left:90px; top:236px; width:155px; height:38px; font-size:21px;">-HARWICK OATES</div>

    <div class="follow" style="left:510px; top:17px; font-size:11px;">FOLLOW US ON</div>
    <div class="social-row" style="left:515px; top:33px; gap:7px;">
      <span class="social-dot" style="width:17px;height:17px;"></span><span class="social-dot" style="width:17px;height:17px;"></span><span class="social-dot" style="width:17px;height:17px;"></span><span class="social-dot" style="width:17px;height:17px;"></span>
    </div>
    <div class="rule-v" style="left:623px; top:15px; width:3px; height:203px;"></div>
    <div class="suburbs" style="left:438px; top:97px; font-size:22px;">- ALEXANDRA HILLS<br>- CAPALABA<br>- SHELDON</div>
    <div class="underline" style="left:452px; top:177px; width:76px; height:4px;"></div>
    <svg class="abs" style="left:455px; top:192px;" width="60" height="75">
      <path d="M4 72 Q38 55 42 22" fill="none" stroke="#fff" stroke-width="1.6" stroke-dasharray="5 4"/>
      <polygon points="43,2 53,30 33,30" fill="#fff"/>
    </svg>
    <div class="cta" style="left:533px; top:288px; height:24px;">
      <div class="cta-icon" style="width:24px;height:24px;"><svg width="12" height="12"><path d="M1 6 H10 M6 2 L10 6 L6 10" stroke="#fff" stroke-width="2" fill="none"/></svg></div>
      <div class="cta-pill" style="width:72px;height:24px;font-size:10.5px;">CONTACT US</div>
    </div>
    <div class="phone-line" style="left:533px; top:314px; font-size:15px;">0491-726-055</div>
    <div class="web-line" style="left:514px; top:332px; font-size:10px;">WWW.YOURWEBSITE.COM</div>
  </section>

  <!-- Profile icon -->
  <div class="size-label" style="left:838px; top:478px;">Profile: 320 x 320 px</div>
  <section class="panel profile-icon" style="left:843px; top:524px; width:320px; height:320px;">
    <div class="portrait" role="img" aria-label="Headshot of the agent in a navy blazer and white shirt" style="left:32px; top:22px; width:258px; height:298px;"></div>
    <div class="wordmark" style="left:0; top:258px; width:148px; height:62px; border:3px solid var(--navy); border-radius:0 16px 0 0; font-size:18px;">HARWICK OATES</div>
    <div class="abs" style="left:148px; top:278px; width:172px; height:42px; background:var(--gold); border:3px solid var(--navy); display:flex; align-items:center; justify-content:center; color:var(--navy); font-weight:500; font-size:21px; white-space:nowrap;">-HARWICK OATES</div>
  </section>

  <!-- Business card -->
  <div class="size-label" style="left:108px; top:940px;">Bussines Card: 820 x 312 px</div>
  <section class="panel business-card" style="left:110px; top:998px; width:1051px; height:600px;">
    <div class="suburb-band"><span>- ALEXANDRA HILLS</span><span>- CAPALABA</span><span>- SHELDON</span></div>
    <div class="portrait" role="img" aria-label="Headshot of the agent in a navy blazer and white shirt" style="left:610px; top:55px; width:441px; height:545px;"></div>
    <div class="wordmark" style="left:0; top:0; width:188px; height:82px; border-radius:0 0 34px 0; font-size:25px;">HARWICK OATES</div>
    <div class="abs" style="left:212px; top:21px; width:801px; height:4px; background:var(--lavender); border-radius:2px;"></div>
    <div class="rule-v" style="left:97px; top:115px; width:7px; height:382px; border-radius:3px;"></div>

    <div class="card-name" style="left:143px; top:108px;">HARWICK OATES</div>
    <div class="underline" style="left:143px; top:185px; width:460px; height:4px;"></div>
    <div class="card-role" style="left:145px; top:195px;">PROPERTY AGENT</div>

    <div class="contact-row" style="top:265px;">
      <div class="contact-dot"><svg width="18" height="18" viewBox="0 0 24 24"><path d="M6.6 10.8a15.1 15.1 0 0 0 6.6 6.6l2.2-2.2a1 1 0 0 1 1-.25 11.4 11.4 0 0 0 3.6.57 1 1 0 0 1 1 1V20a1 1 0 0 1-1 1A17 17 0 0 1 3 4a1 1 0 0 1 1-1h3.5a1 1 0 0 1 1 1c0 1.25.2 2.45.57 3.57a1 1 0 0 1-.25 1z" fill="#141414"/></svg></div>
      <div class="contact-text">0491-726-055</div>
    </div>
    <div class="contact-row" style="top:327px;"><div class="contact-dot"></div><div class="contact-text">YOURFACEBOOK</div></div>
    <div class="contact-row" style="top:389px;"><div class="contact-dot"></div><div class="contact-text">YOURLINKEDIN</div></div>
    <div class="contact-row" style="top:451px;"><div class="contact-dot"></div><div class="contact-text">YOURINSTAGRAM</div></div>
  </section>

  <footer class="footer">
    <div class="footer-left">DESIGN IS STILL EDITABLE</div>
    <div class="footer-right">HARWICK OATES - FACEBOOK COVER PHOTO &amp; PHOTO ICON DESIGN</div>
  </footer>
</div>
</body>
</html>
```